Labels designs for a new coffee brand (Velloru Coffee)

We looking for a coffee label design for our coffee Brand, VELLORU COFFE, attached is the logo. We are bringing out to the market 3 Premium blends
1. Colombian Popayan
2. Gourmet Expresso Blend
3. Brazilian Santos

We like something that looks high quality yet modern, the bags we are using is black matte, we are starting with labels and look in the near future to print our own labels .

We want the labels for the 3 coffees to have the similar look and feel but to be uniquely identified by its design (Colombian, Brazilian, espresso) This is beig sold as a set so we want it to have a similar label feeling but that each is identify as its unique product (colombian, expresso, brazilian blend.

This project is for labels that will be used on a black matte bag, is for a 16 oz bag,

Attached is a sample of the bag color.

Size Requirements:
Maintain a 2:3 aspect ratio for the image file
The label will be 4" wide and 6" tall (we also want to print some 3X4)
Recommended image size is 1600px X 2400px

I will provide upc later

www.vellorucoffee.example pw 12345 this is the test site not live yet but you can get a feel of the brand

Ay my daughters volleyball tournament I need extra time to review

coffee drinkers

coffee

• Creativity, unique, eye catchy,

```html
<!DOCTYPE html>
<html lang="en">
<head>
<meta charset="utf-8">
<title>Velloru Coffee – Label Set</title>
<link href="https://fonts.googleapis.com/css2?family=Antonio:wght@200;300&family=Josefin+Sans:wght@400&display=swap" rel="stylesheet">
<style>
  :root {
    --canvas-bg: #f4ebe4;
    --canvas-glow: #efdccf;
    --cream: #e6e0db;
    --cream-light: #ece8e4;
    --title: #cf9468;
    --espresso: #b8403f;
    --espresso-light: #d4716f;
    --brazil: #4e8467;
    --brazil-light: #85b39a;
    --colombia: #5a6e96;
    --colombia-light: #8a9bbc;
  }
  * { box-sizing: border-box; margin: 0; padding: 0; }
  html, body { width: 1200px; height: 720px; overflow: hidden; }
  body {
    background: radial-gradient(ellipse at center, var(--canvas-glow) 0%, var(--canvas-bg) 55%, #fbf8f6 100%);
    font-family: "Antonio", sans-serif;
  }
  .label-set {
    display: flex;
    justify-content: center;
    gap: 60px;
    padding-top: 135px;
  }
  .label {
    position: relative;
    width: 300px;
    height: 450px;
    background: linear-gradient(160deg, var(--cream-light), var(--cream));
    overflow: hidden;
    box-shadow: 0 6px 18px rgba(0,0,0,.12);
  }
  .label__pattern {
    position: absolute;
    inset: 0 0 auto 0;
    height: 230px;
    background: radial-gradient(circle at 55% 70%, var(--tone-light) 0%, var(--tone) 70%);
  }
  .label__badge {
    position: absolute;
    left: 50%;
    top: 188px;
    width: 84px;
    height: 84px;
    margin-left: -42px;
    border-radius: 50%;
    background: var(--tone-light);
  }
  .label__name {
    position: absolute;
    left: 0; right: 0;
    top: 285px;
    text-align: center;
    font-weight: 200;
    font-size: 34px;
    line-height: 1;
    letter-spacing: 0.5px;
    color: var(--title);
    text-transform: uppercase;
  }
  .label__brand {
    position: absolute;
    left: 0; right: 0;
    bottom: 20px;
    display: flex;
    justify-content: center;
    align-items: center;
    gap: 5px;
    font-family: "Josefin Sans", sans-serif;
    font-size: 14px;
    letter-spacing: 2px;
    color: var(--tone);
  }
  .label__brand-dot {
    width: 9px; height: 9px;
    border-radius: 50%;
    background: var(--tone);
  }
  .label--espresso { --tone: var(--espresso); --tone-light: var(--espresso-light); }
  .label--brazil { --tone: var(--brazil); --tone-light: var(--brazil-light); }
  .label--colombia { --tone: var(--colombia); --tone-light: var(--colombia-light); }
  .label--espresso .label__name { top: 285px; }
  .label--brazil .label__name,
  .label--colombia .label__name { top: 300px; }
</style>
</head>
<body>
  <main class="label-set">
    <article class="label label--espresso">
      <div class="label__pattern" role="img" aria-label="Hand-drawn coffee bean line pattern on red"></div>
      <div class="label__badge"></div>
      <h2 class="label__name">Gourmet<br>Expresso<br>Blend</h2>
      <p class="label__brand"><span class="label__brand-dot"></span>VELLORU</p>
    </article>
    <article class="label label--brazil">
      <div class="label__pattern" role="img" aria-label="Hand-drawn coffee bean line pattern on green"></div>
      <div class="label__badge"></div>
      <h2 class="label__name">Brazilian<br>Santos</h2>
      <p class="label__brand"><span class="label__brand-dot"></span>VELLORU</p>
    </article>
    <article class="label label--colombia">
      <div class="label__pattern" role="img" aria-label="Hand-drawn coffee bean line pattern on blue"></div>
      <div class="label__badge"></div>
      <h2 class="label__name">Colombian<br>Popayan</h2>
      <p class="label__brand"><span class="label__brand-dot"></span>VELLORU</p>
    </article>
  </main>
</body>
</html>
```